" Empresa em abertura de firma (status), voltada para o segmento de Headhunter / Jobhunter, Coaching e demais serviços administrativos/treinamento relacionados. "

```html
<!DOCTYPE html>
<html lang="pt-BR">
<head>
<meta charset="UTF-8">
<title>TopRecruta – Adesivo</title>
<link rel="stylesheet" href="https://fonts.googleapis.com/css2?family=Open+Sans:wght@600;700&display=swap">
<style>
  :root {
    --page-bg: #eef0f3;
    --sticker-face: #ffffff;
    --ring-light: #6f9be0;
    --ring-dark: #1f4ea8;
    --brand-blue: #2b4c9b;
    --text-dark: #1f2a44;
    --icon-blue: #2f66c4;
    --icon-gold: #f2c318;
  }
  * { margin: 0; padding: 0; box-sizing: border-box; }
  html, body {
    width: 1200px;
    height: 1200px;
    overflow: hidden;
    background: var(--page-bg);
    font-family: "Open Sans", Arial, sans-serif;
  }
  .canvas {
    position: relative;
    width: 1200px;
    height: 1200px;
    display: flex;
    align-items: center;
    justify-content: center;
  }
  .sticker {
    position: relative;
    width: 1000px;
    height: 1000px;
    border-radius: 50%;
    background: radial-gradient(circle at 35% 25%, var(--ring-light), var(--ring-dark) 75%);
    padding: 26px;
    box-shadow: 0 6px 18px rgba(0, 0, 0, 0.12);
  }
  .sticker-face {
    width: 100%;
    height: 100%;
    border-radius: 50%;
    background: var(--sticker-face);
    display: flex;
    flex-direction: column;
    align-items: center;
    justify-content: center;
    padding-top: 40px;
  }
  .brand {
    display: flex;
    align-items: center;
    gap: 26px;
  }
  .brand-dot {
    width: 70px;
    height: 70px;
    border-radius: 50%;
    background: var(--brand-blue);
  }
  .brand-name {
    font-size: 124px;
    font-weight: 700;
    color: var(--brand-blue);
    letter-spacing: -2px;
    line-height: 1;
  }
  .contacts {
    margin-top: 110px;
    display: flex;
    flex-direction: column;
    gap: 34px;
  }
  .contact-row {
    display: flex;
    align-items: center;
    gap: 24px;
    font-size: 40px;
    font-weight: 600;
    color: var(--text-dark);
  }
  .contact-icon {
    width: 56px;
    height: 56px;
    flex: none;
  }
  .social-mark {
    width: 52px;
    height: 52px;
    flex: none;
    margin: 2px;
    border: 5px solid var(--icon-gold);
    border-radius: 10px;
  }
</style>
</head>
<body>
<main class="canvas">
  <section class="sticker">
    <div class="sticker-face">
      <div class="brand">
        <span class="brand-dot"></span>
        <span class="brand-name">TopRecruta</span>
      </div>
      <div class="contacts">
        <div class="contact-row">
          <svg class="contact-icon" viewBox="0 0 24 24" aria-hidden="true">
            <path fill="var(--icon-blue)" d="M6.6 10.8a15.1 15.1 0 0 0 6.6 6.6l2.2-2.2c.3-.3.7-.4 1-.2 1.1.4 2.3.6 3.6.6.6 0 1 .4 1 1V20c0 .6-.4 1-1 1A17 17 0 0 1 3 4c0-.6.4-1 1-1h3.5c.6 0 1 .4 1 1 0 1.3.2 2.5.6 3.6.1.3 0 .7-.2 1z"/>
          </svg>
          <span class="contact-text">00 0000-0000 | 00 0000-0000</span>
        </div>
        <div class="contact-row">
          <span class="social-mark"></span>
          <span class="contact-text">@toprecruta</span>
        </div>
      </div>
    </div>
  </section>
</main>
</body>
</html>
```